Vireon Spool Business Card Design

This is a start up company that has state of the art patented technology for turbo chargers,that can be used on engines, gas or diesel, for any type of automotive,aviation,marine or industrial purpose.
This technology will provide longer life,lower maintenance and better performance and help produce lower emissions with any turbocharged engine.Red would be a predominate color and the design should communicate the latest technology,economy and
Environmental concern.
This product will initially be distributed in the U.S.A. But should move rapidly to global use.
Updates

Thank you for your design submissions, I have increased the budget for this job because my initial order was too low for the quality of work shown, plus I would Like to see some more options. I have a meeting this Sunday with my other partners and would anticipate being able to give you some feedback by the Beginning of next week. Regards.

Thank you for everyone's participation. The deadline is still open until 6/15 and my partners and I have a meeting Scheduled this weekend. At this time we have not ruled anyone out, But will be making a decision during the course of our meeting and wil Decide which direction we will be going in by the beginning of the week. Thanks again, regards, Tom Brandt.

Hello everybody, Sorry for the delay in communication, we have been very busy in putting the start up together. We are still not decided on the design of the business card and have a wide range to choose from. I would anticipated we shall have an answer within the next two weeks. Regards, Tom Brandt.

Target Market(s)

Manufacturers and wholesalers' of OEM and replacement turbochargers

Industry/Entity Type

Industrial

Contact Information for Business Card

We need a logo that should incorporate the " Vireon, a " possibly super imposed over a turbo charger with the fan blades of the turbocharger showing in the center of the "a" .
Name,title,phone number and email address only, no street/mailing address at this time.
The full name of the company is
" Vireon Spool Dynamics LLC "
For the initial card you can use my info.
Thomas Brandt
VP Sales & Marketing
tbrandt@vireonspooldyn.example
555 014 2286

Requirements
Must have
• The Vireon A, the outline of a turbo charger
Nice to have
• Something classy and simple and worldly (global)
Should not have
• No engines,cars,boats,planes

```html
<!DOCTYPE html>
<html lang="en">
<head>
<meta charset="utf-8">
<title>Vireon Spool Dynamics – Business Card</title>
<link rel="stylesheet" href="https://fonts.googleapis.com/css2?family=Roboto:wght@300;400;700&display=swap">
<style>
  :root {
    --page-bg: #e9e7e4;
    --card-white: #f7f7f7;
    --card-grey: #ebebeb;
    --ink: #1d1d1d;
    --brand-red: #a3141c;
    --brand-red-dark: #7d0c12;
    --icon-grey: #b5b5b5;
    --icon-warm: #c98a74;
  }
  * { box-sizing: border-box; margin: 0; padding: 0; }
  html, body {
    width: 1200px; height: 1000px; overflow: hidden;
    background: var(--page-bg);
    font-family: "Roboto", Arial, sans-serif;
  }
  .card {
    position: absolute; left: 350px; top: 60px;
    width: 500px; height: 880px;
    background: linear-gradient(180deg, var(--card-white) 0%, var(--card-grey) 100%);
    box-shadow: 0 6px 24px rgba(0,0,0,0.18);
    display: flex; flex-direction: column; align-items: center;
    overflow: hidden;
  }
  .brand {
    margin-top: 70px;
    display: flex; align-items: center; gap: 16px;
  }
  .brand-dot {
    width: 58px; height: 58px; border-radius: 50%;
    background: var(--brand-red);
  }
  .brand-name {
    font-weight: 700; font-size: 30px; color: var(--ink);
    letter-spacing: 0.2px;
  }
  .rule {
    width: 420px; height: 2px; background: var(--brand-red);
    margin-top: 26px; opacity: 0.8;
  }
  .person-name {
    margin-top: 18px;
    font-size: 54px; font-weight: 400; color: var(--brand-red);
  }
  .detail-icon { margin-top: 24px; width: 30px; height: 30px; }
  .detail {
    margin-top: 8px;
    font-size: 30px; font-weight: 300; color: var(--ink);
  }
  .care-emblem {
    margin-top: 30px;
    width: 92px; height: 72px; border-radius: 10px;
    background: var(--icon-warm); opacity: 0.85;
  }
  .web-band {
    position: absolute; left: 0; bottom: 0;
    width: 100%; height: 140px;
    background: linear-gradient(90deg, var(--brand-red) 0%, var(--brand-red-dark) 100%);
    display: flex; align-items: center; justify-content: center;
  }
  .web-address {
    font-size: 30px; font-weight: 300; color: #f3dede;
  }
</style>
</head>
<body>
  <article class="card">
    <header class="brand">
      <span class="brand-dot"></span>
      <span class="brand-name">Vireon Spool Dynamics LLC</span>
    </header>
    <div class="rule"></div>
    <h1 class="person-name">Thomas Brandt</h1>

    <svg class="detail-icon" viewBox="0 0 30 30" aria-hidden="true">
      <circle cx="15" cy="15" r="15" fill="var(--icon-grey)"/>
      <circle cx="15" cy="12" r="5" fill="#fff"/>
      <path d="M6.5 24c1.5-5 4.5-6.5 8.5-6.5s7 1.5 8.5 6.5z" fill="#fff"/>
    </svg>
    <p class="detail">VP Sales &amp; Marketing</p>

    <svg class="detail-icon" viewBox="0 0 30 30" aria-hidden="true">
      <circle cx="15" cy="15" r="15" fill="var(--icon-grey)"/>
      <path d="M10 7.5l3 0 1.5 4-2 1.5c1 2.3 2.5 3.8 4.5 4.5l1.5-2 4 1.5v3c0 1-1 2-2 2-7 0-12.5-5.5-12.5-12.5 0-1 1-2 2-2z" fill="#fff"/>
    </svg>
    <p class="detail">555.014.2286</p>

    <svg class="detail-icon" viewBox="0 0 30 30" aria-hidden="true">
      <circle cx="15" cy="15" r="15" fill="var(--icon-grey)"/>
      <rect x="7.5" y="9.5" width="15" height="11" fill="#fff"/>
      <path d="M7.5 9.5l7.5 6 7.5-6" fill="none" stroke="var(--icon-grey)" stroke-width="1.4"/>
    </svg>
    <p class="detail">tbrandt@vireonspooldyn.example</p>

    <div class="care-emblem" role="img" aria-label="Emblem of two open hands holding a globe"></div>

    <footer class="web-band">
      <span class="web-address">www.vireonspooldyn.example</span>
    </footer>
  </article>
</body>
</html>
```